Letterhead for New Orthopaedic Surgery Practice

My husband and I are starting our own practice named RB Spine & Vitality Center. We would like to create a nice simple but high class letterhead that doesn't use too much solid color ink when printing. I like the colors dark blue, gold, yellow. Open to other suggestions. We will need to list him and I both on the top of the letterhead. Here is the important information:
Lucinda Pryce, M.D. - Hand and Upper Extremity Surgery
Esi Dankwa, M.D. - Hip & Knee Replacement/General Orthopaedic Surgery
Location: 18735 North Bellhaven Rd
Coral Springs, FL 33071
Phone: 954-218-4635
Fax: 954-581-2264
Email: info@myrbspine.example

The only thing is that the phone and fax numbers will change once we get into our space. I just want to get the design started. I am including several documents which are my previous practice letterhead, my current procedure room letterhead, and our new Logo. The other letterheads are just for examples but please think outside of the box! We would love to see some great designs.

Colors
0054AA
0677BA
7BADD7
CADEEF
E8F1F8
0094D4
00A9DD
6FCCEA
C7EBF8
E9F6FB

Requirements
Must have
• class, elegance, luxury

```html
<!DOCTYPE html>
<html lang="en">
<head>
<meta charset="utf-8">
<title>RB Spine &amp; Vitality Center — Letterhead</title>
<link href="https://fonts.googleapis.com/css2?family=Marcellus&family=Roboto:wght@400;500&family=Varela+Round&display=swap" rel="stylesheet">
<style>
  :root {
    --navy: #2f4b8c;
    --navy-dark: #263f7a;
    --cyan: #33bfe0;
    --text-grey: #6e6e6e;
    --meta-grey: #555a62;
    --paper: #f7f7f7;
    --backdrop: #e4e4e4;
    --signature-tone: #e6e7ea;
  }
  * { box-sizing: border-box; margin: 0; padding: 0; }
  html, body { width: 1058px; height: 1200px; overflow: hidden; }
  body { background: var(--backdrop); position: relative; }

  .letterhead {
    position: absolute; left: 120px; top: 20px;
    width: 818px; height: 1160px;
    background: var(--paper);
    box-shadow: 0 2px 10px rgba(0,0,0,0.12);
    font-family: 'Varela Round', sans-serif;
    color: var(--text-grey);
  }
  .top-band { position: absolute; left: 0; top: 0; width: 818px; height: 16px; display: block; }

  .brand {
    position: absolute; left: 79px; top: 72px; width: 240px;
    display: flex; align-items: center; gap: 10px;
  }
  .brand-mark { width: 14px; height: 14px; border-radius: 50%; background: var(--navy); flex: none; }
  .brand-name {
    font-family: 'Marcellus', serif; font-size: 20px; line-height: 24px;
    color: var(--navy); letter-spacing: 0.3px;
  }

  .physicians {
    position: absolute; right: 262px; top: 70px; text-align: right;
    font-family: 'Roboto', sans-serif;
  }
  .physician-name { font-size: 13.5px; font-weight: 500; color: var(--navy); line-height: 17px; }
  .physician-specialty { font-size: 12px; color: var(--meta-grey); line-height: 15px; }
  .physician + .physician { margin-top: 5px; }

  .divider { position: absolute; left: 571px; top: 70px; width: 1px; height: 89px; background: var(--cyan); }

  .contact {
    position: absolute; left: 585px; top: 71px; list-style: none;
    font-family: 'Roboto', sans-serif; font-size: 12px; color: var(--meta-grey);
  }
  .contact li { display: flex; align-items: flex-start; line-height: 15.5px; margin-bottom: 2px; }
  .contact svg { width: 12px; height: 12px; margin-top: 2px; margin-right: 7px; flex: none; fill: var(--navy); }
  .contact .address { margin-bottom: 3px; }

  .letter-body {
    position: absolute; left: 79px; top: 312px; width: 656px;
    font-size: 13.3px; line-height: 19px;
  }
  .letter-body p { margin-bottom: 19px; text-align: justify; }
  .letter-body .salutation { text-align: left; }
  .closing { margin-top: 0; }
  .sender { margin-top: 38px; }

  .signature-area {
    position: absolute; left: 79px; top: 889px; width: 82px; height: 76px;
    background: var(--signature-tone); border-radius: 4px;
  }

  .footer {
    position: absolute; left: 0; top: 1102px; width: 818px;
    display: flex; justify-content: center; align-items: center;
    font-family: 'Roboto', sans-serif; font-size: 13px; color: var(--meta-grey);
  }
  .footer-rule { width: 60px; height: 1.5px; background: var(--navy); margin: 0 12px; }
  .footer svg { width: 11px; height: 11px; margin: 0 5px; fill: var(--navy); }
</style>
</head>
<body>
  <main class="letterhead">
    <svg class="top-band" viewBox="0 0 818 16" aria-hidden="true">
      <rect x="0" y="0" width="818" height="16" fill="var(--navy)"/>
      <polygon points="671,0 818,0 818,16 657,16" fill="var(--cyan)"/>
      <polygon points="668,0 671,0 657,16 654,16" fill="#ffffff"/>
    </svg>

    <div class="brand">
      <span class="brand-mark"></span>
      <span class="brand-name">RB Spine &amp; Vitality<br>Center</span>
    </div>

    <div class="physicians">
      <div class="physician">
        <div class="physician-name">Lucinda Pryce, M.D.</div>
        <div class="physician-specialty">Hand &amp; Upper Extremity Surgeon</div>
      </div>
      <div class="physician">
        <div class="physician-name">Esi Dankwa, M.D.</div>
        <div class="physician-specialty">Hip &amp; Knee Replacement/</div>
        <div class="physician-specialty">General Orthopaedic Surgeon</div>
      </div>
    </div>

    <div class="divider"></div>

    <ul class="contact">
      <li class="address">
        <svg viewBox="0 0 12 12"><path d="M6 0C3.6 0 2 1.8 2 4c0 3 4 8 4 8s4-5 4-8c0-2.2-1.6-4-4-4zm0 5.6A1.6 1.6 0 1 1 6 2.4a1.6 1.6 0 0 1 0 3.2z"/></svg>
        <span>18735 North Bellhaven Rd<br>Coral Springs, FL 33071</span>
      </li>
      <li>
        <svg viewBox="0 0 12 12"><path d="M1 4c0-1.5 2-2.5 5-2.5S11 2.5 11 4v1H8.5V3.8h-5V5H1zM3 6l1-1.5h4L9 6l1.5 4.5h-9zM6 7a1.3 1.3 0 1 0 0 2.6A1.3 1.3 0 0 0 6 7z"/></svg>
        <span>954-218-4635</span>
      </li>
      <li>
        <svg viewBox="0 0 12 12"><path d="M3 1h6v3H3zM1 5h10v5H9V8H3v2H1zM3.5 9h5v2h-5z"/></svg>
        <span>954-581-2264</span>
      </li>
      <li>
        <svg viewBox="0 0 12 12"><path d="M1 2.5h10v1L6 6.5 1 3.5zM1 5l5 3 5-3v4.5H1z"/></svg>
        <span>info@myrbspine.example</span>
      </li>
    </ul>

    <article class="letter-body">
      <p class="salutation">Dear customer,</p>
      <p>Lorem ipsum dolor sit amet, consectetur adipisicing elit, sed do eiusmod tempor incididunt ut labore et dolore magna aliqua. Ut enim ad minim veniam, quis nostrud exercitation ullamco laboris nisi ut aliquip ex ea commodo consequat. Duis aute irure dolor in reprehenderit in voluptate velit esse cillum dolore eu fugiat nulla pariatur. Excepteur sint occaecat cupidatat non proident, sunt in culpa qui officia deserunt mollit anim id est laborum.</p>
      <p>Lorem ipsum dolor sit amet, consectetur adipisicing elit, sed do eiusmod tempor incididunt ut labore et dolore magna aliqua. Ut enim ad minim veniam, quis nostrud exercitation ullamco laboris nisi ut aliquip ex ea commodo consequat. Duis aute irure dolor in reprehenderit in voluptate velit esse cillum dolore eu fugiat nulla pariatur. Excepteur sint occaecat cupidatat non proident, sunt in culpa qui officia deserunt mollit anim id est laborum.</p>
      <p>Lorem ipsum dolor sit amet, consectetur adipisicing elit, sed do eiusmod tempor incididunt ut labore et dolore magna aliqua. Ut enim ad minim veniam, quis nostrud exercitation ullamco laboris nisi ut aliquip ex ea commodo consequat. Duis aute irure dolor in reprehenderit in voluptate velit esse cillum dolore eu fugiat nulla pariatur. Excepteur sint occaecat cupidatat non proident, sunt in culpa qui officia deserunt mollit anim id est laborum.</p>
      <p>Lorem ipsum dolor sit amet, consectetur adipisicing elit, sed do eiusmod tempor incididunt ut labore et dolore magna aliqua. Ut enim ad minim veniam, quis nostrud exercitation ullamco laboris nisi ut aliquip ex ea commodo consequat. Duis aute irure dolor in reprehenderit.</p>
      <p class="salutation closing">Yours Sincerely,</p>
      <p class="salutation sender">Marcus Hale<br>General Director</p>
    </article>

    <div class="signature-area" role="img" aria-label="Handwritten signature of the sender"></div>

    <footer class="footer">
      <span class="footer-rule"></span>
      <span>www.lprycehand.example</span>
      <svg viewBox="0 0 12 12"><circle cx="6" cy="6" r="5.5"/><path d="M3 4.5h2.5l1 1.5-1 1.5 1 2M7.5 2.5 8 4l1.5.5" stroke="#f7f7f7" stroke-width="1" fill="none"/></svg>
      <span>www.dankwahipandknee.example</span>
      <span class="footer-rule"></span>
    </footer>
  </main>
</body>
</html>
```